Medical program Ombo produce by VALORENZA

I need a business card of the program to give to the customer to get the general information to contact the clinic. I need a bilingual card French and English you will see the logo.
That's a program that the Clinic Valorenza offers. https://medicalombo.ca
Program: Ombo Medical Program
Slogan: Lose weight - Exist - Live / FEEL LIGHT - MOVE - THRIVE
The clinic that offers the program: Valorenza
Website: https://medicalombo.ca
---
Medical team / Medical team
email: doc@valorenza.ca
phone: 514 555-0147
Information
email: ombo@valorenza.ca
phone: 514 555-0183 ext 3
Target Market(s)
Every person that needs to lose weight
Industry/Entity Type
Health clinic for obese person
Contact Information for Business Card
All the information in the description
Requirements
Must have
- Look clean - Expensive clinic / Need to be bilingual
Nice to have
- Recto verso for french and english
Should not have
- -

```html
<!DOCTYPE html>
<html lang="en">
<head>
<meta charset="UTF-8">
<title>Medical Ombo – Business Card</title>
<link href="https://fonts.googleapis.com/css2?family=Poppins:wght@400;600;700&display=swap" rel="stylesheet">
<style>
  :root {
    --backdrop: #0d0d0e;
    --card: #2a2b2e;
    --band: #0a7fd4;
    --blue: #1386d6;
    --teal: #1aa6a0;
    --text: #f2f2f2;
    --accent-red: #d9353d;
  }
  * { box-sizing: border-box; margin: 0; padding: 0; }
  html, body {
    width: 1200px; height: 820px; overflow: hidden;
    background: var(--backdrop);
    font-family: "Poppins", sans-serif;
  }
  .stage {
    position: relative; width: 1200px; height: 820px;
    display: flex; align-items: center; justify-content: center; gap: 40px;
  }
  .card {
    position: relative; width: 520px; height: 300px;
    background: var(--card);
    overflow: hidden;
  }
  .card::after {
    content: ""; position: absolute; left: 0; right: 0; bottom: 0;
    height: 9px; background: var(--band);
  }

  /* Front */
  .brand-lockup {
    position: absolute; top: 40px; right: 62px; text-align: right;
  }
  .brand-name {
    font-size: 42px; font-weight: 400; color: var(--teal);
    letter-spacing: 1px; line-height: 1; white-space: nowrap;
  }
  .brand-slogan {
    margin-top: 8px; font-size: 8px; letter-spacing: 3px;
    color: var(--teal); text-transform: uppercase; white-space: nowrap;
  }
  .contact {
    position: absolute; color: var(--text);
    font-size: 14px; line-height: 1.4; white-space: nowrap;
  }
  .contact h3 {
    font-size: 15px; font-weight: 700; text-transform: uppercase;
    letter-spacing: .5px; line-height: 1.4;
  }
  .contact-team { left: 34px; bottom: 34px; }
  .contact-team h3 { color: var(--blue); }
  .contact-info { right: 34px; bottom: 34px; text-align: right; }
  .contact-info h3 { color: var(--teal); }
  .line { display: flex; align-items: center; gap: 7px; }
  .contact-info .line { justify-content: flex-end; }
  .icon { width: 12px; height: 12px; flex: none; }
  .contact-team .icon { fill: var(--blue); }
  .contact-info .icon { fill: var(--teal); }
  .web { margin-top: 2px; }

  /* Back */
  .clinic-lockup {
    position: absolute; right: 44px; top: 96px; text-align: center;
  }
  .clinic-name {
    display: flex; align-items: center; gap: 12px;
    font-size: 34px; font-weight: 700; color: var(--text);
    letter-spacing: .5px; line-height: 1.1; white-space: nowrap;
  }
  .clinic-mark { width: 26px; height: 26px; background: var(--accent-red); }
  .clinic-web { margin-top: 10px; font-size: 14px; color: var(--text); }
</style>
</head>
<body>
<main class="stage">
  <section class="card card-front">
    <div class="brand-lockup">
      <div class="brand-name">Medical Ombo</div>
      <div class="brand-slogan">Feel light - Move - Thrive</div>
    </div>

    <div class="contact contact-team">
      <h3>Medical Team</h3>
      <p class="line">
        <svg class="icon" viewBox="0 0 16 16"><path d="M1 3h14L8 8.5z"/><path d="M1 4.5l7 5.5 7-5.5V13H1z"/></svg>
        doc@valorenza.ca
      </p>
      <p class="line">
        <svg class="icon" viewBox="0 0 16 16"><path d="M3 1l3 3-1.5 2a9 9 0 0 0 5.5 5.5L12 10l3 3-2 2C7 15 1 9 1 3z"/></svg>
        514 555-0147
      </p>
      <p class="web">www.medicalombo.ca</p>
    </div>

    <div class="contact contact-info">
      <h3>Information</h3>
      <p class="line">
        ombo@valorenza.ca
        <svg class="icon" viewBox="0 0 16 16"><path d="M1 3h14L8 8.5z"/><path d="M1 4.5l7 5.5 7-5.5V13H1z"/></svg>
      </p>
      <p class="line">
        514 555-0183 ext 3
        <svg class="icon" viewBox="0 0 16 16"><path d="M3 1l3 3-1.5 2a9 9 0 0 0 5.5 5.5L12 10l3 3-2 2C7 15 1 9 1 3z"/></svg>
      </p>
      <p class="web">www.medicalombo.ca</p>
    </div>
  </section>

  <section class="card card-back">
    <div class="clinic-lockup">
      <div class="clinic-name"><span class="clinic-mark"></span>VALORENZA</div>
      <div class="clinic-web">www.medicalombo.ca</div>
    </div>
  </section>
</main>
</body>
</html>
```